Main Banner for Hullwrap.com, SIMPLE REDESIGN

We need to redesign the main banner that appears on the homepage of our website.

Attached in the project brief is a reference.

There are alot of things we like that we want to keep from that concept but its overall just something I drew on paint and not designed well.

1. Keep yellow tabs on the right hand side, we want them bigger and bolder and to showcase the bullet points inside.
2. Get rid of the 10 yr warranty emblem and replace that with our Brandell logo also attached to the brief.
3. Keep the bottom header and include hullwrap.com and the phone number, but make it look bolder and nicer.
4. Keep the watermark

Aside from these points what we really need is this but a better cleaner more professional version of it.

Target Market(s)

Visitors to our website hullwrap.com we want this banner to include all the major selling points, branding of the product and info on how to contact us.

Requirements
Must have
• Must be clean and professional. My fear is getting submissions that are too busy or messy. There are a lot of components but the challenge is to put them all in there in a clean professional way.
Should not have
• An image in the background like a beach or some kind of picture want the focus to be the requirements listed in the project description

```html
<!DOCTYPE html>
<html lang="en">
<head>
<meta charset="utf-8">
<title>Brandell Supreme Boat Cover – Hullwrap.com Banners</title>
<link rel="stylesheet" href="https://fonts.googleapis.com/css2?family=Open+Sans:wght@700;800&display=swap">
<style>
  :root {
    --navy: #0b2266;
    --yellow: #fcc812;
    --tab-text: #1e1e1e;
    --white: #ffffff;
    --bg-light: #f7f8fa;
    --bg-edge: #d9dde3;
    --frame: #cfd2d6;
    --cover-grey: #a3a6a4;
    --hull-white: #e9ecef;
  }
  * { margin: 0; padding: 0; box-sizing: border-box; }
  html, body {
    width: 1200px; height: 1000px; overflow: hidden;
    background: var(--white);
    font-family: "Open Sans", Arial, sans-serif;
  }
  .canvas { position: relative; width: 1200px; height: 1000px; }

  .banner {
    position: absolute;
    width: 755px; height: 346px;
    overflow: hidden;
    border: 1px solid var(--frame);
    background: radial-gradient(ellipse at 45% 40%, var(--white) 0%, var(--bg-light) 45%, var(--bg-edge) 100%);
  }
  .banner--stacked { left: 227px; top: 122px; }
  .banner--wide { left: 231px; top: 524px; }

  .banner__title {
    position: absolute;
    color: var(--navy);
    font-weight: 800;
    font-size: 32px;
    line-height: 33px;
    letter-spacing: 0.5px;
  }
  .banner--stacked .banner__title { right: 32px; top: 20px; text-align: right; }
  .banner--wide .banner__title { left: 0; right: 0; top: 16px; text-align: center; }

  .product-photo {
    position: absolute;
    border-radius: 40px 60px 20px 20px;
    background: linear-gradient(180deg, var(--cover-grey) 0%, var(--cover-grey) 55%, var(--hull-white) 56%, #cfd4d9 100%);
    opacity: 0.9;
  }
  .banner--stacked .product-photo { left: 14px; top: 34px; width: 484px; height: 258px; }
  .banner--wide .product-photo { left: 34px; top: 64px; width: 460px; height: 228px; }

  .tab {
    position: absolute;
    right: 0;
    height: 44px;
    background: var(--yellow);
    clip-path: polygon(0 0, 100% 0, 100% 100%, 24px 100%);
    color: var(--tab-text);
    font-weight: 800;
    font-size: 22px;
    line-height: 44px;
    text-align: right;
    padding-right: 27px;
    letter-spacing: 0.3px;
  }
  .banner--stacked .tab--warranty { top: 107px; width: 296px; }
  .banner--stacked .tab--shipping { top: 170px; width: 261px; }
  .banner--stacked .tab--waterproof { top: 233px; width: 227px; padding-right: 20px; }
  .banner--wide .tab--warranty { top: 87px; width: 294px; }
  .banner--wide .tab--shipping { top: 150px; width: 259px; }
  .banner--wide .tab--waterproof { top: 213px; width: 224px; padding-right: 17px; }

  .contact-bar {
    position: absolute;
    left: 0; right: 0; bottom: 0;
    height: 52px;
    background: var(--navy);
    color: var(--white);
    font-weight: 800;
    font-size: 22px;
    line-height: 52px;
  }
  .contact-bar__url { position: absolute; left: 43px; }
  .contact-bar__phone { position: absolute; right: 30px; }
  .contact-bar__brand {
    position: absolute;
    left: 50%; transform: translateX(-50%);
    font-size: 16px;
    letter-spacing: 0.5px;
  }
</style>
</head>
<body>
<div class="canvas">

  <section class="banner banner--stacked">
    <div class="product-photo" role="img" aria-label="Boat on a twin-axle trailer wrapped in a grey fitted cover with black tie-down straps"></div>
    <h1 class="banner__title">BRANDELL SUPREME<br>BOAT COVER</h1>
    <div class="tab tab--warranty">10 YR WARRANTY</div>
    <div class="tab tab--shipping">FREE SHIPPING</div>
    <div class="tab tab--waterproof">WATERPROOF</div>
    <div class="contact-bar">
      <span class="contact-bar__url">WWW.HULLWRAP.COM</span>
      <span class="contact-bar__brand">BRANDELL</span>
      <span class="contact-bar__phone">CALL US AT: 800-555-0142</span>
    </div>
  </section>

  <section class="banner banner--wide">
    <div class="product-photo" role="img" aria-label="Boat on a twin-axle trailer wrapped in a grey fitted cover with black tie-down straps"></div>
    <h1 class="banner__title">BRANDELL SUPREME BOAT COVER</h1>
    <div class="tab tab--warranty">10 YR WARRANTY</div>
    <div class="tab tab--shipping">FREE SHIPPING</div>
    <div class="tab tab--waterproof">WATERPROOF</div>
    <div class="contact-bar">
      <span class="contact-bar__url">WWW.HULLWRAP.COM</span>
      <span class="contact-bar__brand">BRANDELL</span>
      <span class="contact-bar__phone">CALL US AT: 800-555-0142</span>
    </div>
  </section>

</div>
</body>
</html>
```